Android Payment Application UI Design

We require a UI/UX design for an existing Android card-based payment application.

We're looking to improve the look + feel of the existing app. What we're after:
- Colour palette options
- Fonts
- Icons

See attached document for existing screen types, icons, etc.

All resources provided must be royalty free.

It's to run on a specialised device, with 720 x 1280 pixel resolution, in portrait only (landscape not required).

Please provide mockup examples of the new screen layout applied to the existing screens in the document.

Target Market(s)

Retail business users

Font styles to use
Sans Serif

Colors

Designer to choose colors to be used in the design.

Requirements
Must have
• Looking for
• - modern design
• - simple colours, easy-to-read sans-serif fonts
• - cohesive, consistent design between screens

```html
<!DOCTYPE html>
<html lang="en">
<head>
<meta charset="utf-8">
<title>PayNova Terminal Screens</title>
<link href="https://fonts.googleapis.com/css2?family=Poppins:wght@300;400;500;600;700&display=swap" rel="stylesheet">
<style>
:root{
  --bg:#b9b9b9;
  --screen:#ffffff;
  --navy:#1d1748;
  --blue:#1a9ad6;
  --key-red:#e3000f;
  --key-yellow:#ffc400;
  --key-green:#1b6e2b;
  --ok:#2ecc8f;
  --busy:#0099dd;
  --fail:#e84a4f;
  --grey:#8a8a8a;
  --line:#e6e6e6;
}
*{box-sizing:border-box;margin:0;padding:0}
html,body{width:930px;height:1200px;overflow:hidden;background:var(--bg);font-family:'Poppins',sans-serif;color:var(--navy)}
.screen{position:absolute;width:214px;height:380px;background:var(--screen);overflow:hidden}
.c1{left:15px}.c2{left:244px}.c3{left:473px}.c4{left:702px}
.r1{top:15px}.r2{top:410px}.r3{top:806px}
.status{position:absolute;top:4px;right:5px;font-size:6px;color:var(--grey);display:flex;gap:3px;align-items:center}
.status i{display:inline-block;width:5px;height:6px;background:#999}
.header{position:relative;height:48px;display:flex;align-items:center;justify-content:center;box-shadow:0 1px 3px rgba(0,0,0,.06);background:#fff;z-index:2}
.brand{display:flex;align-items:center;gap:5px;font-weight:700;font-size:19px;letter-spacing:1px;color:var(--navy);margin-top:6px}
.brand b{width:14px;height:14px;border-radius:50%;background:var(--blue)}
.menu{position:absolute;right:12px;top:24px;width:13px}
.menu span{display:block;height:1px;background:#999;margin-bottom:3px}
.battery{position:absolute;left:10px;top:25px;width:12px;height:6px;border:1.5px solid #f08a00;border-radius:1px}
.title{padding:0 19px;font-weight:700;font-size:14px;line-height:1}
.sub{padding:0 19px;font-weight:500;font-size:10px;margin-top:2px}
.field{margin:0 19px;border-bottom:2px solid var(--blue);color:var(--blue);font-size:16px;text-align:center;font-weight:300;line-height:1.4}
.keypad{position:absolute;left:0;bottom:0;width:214px;height:142px;display:grid;grid-template-columns:repeat(4,1fr);grid-template-rows:35px 35px 36px 36px;background:var(--navy)}
.keypad div{display:flex;align-items:center;justify-content:center;color:#fff;font-size:13px;border-right:1px solid #24428c;border-bottom:1px solid #24428c}
.keypad .zero{grid-column:4;grid-row:1/4;border-right:0}
.keypad .k-x{background:var(--key-red);border:0}
.keypad .k-back{background:var(--key-yellow);border:0}
.keypad .k-enter{background:var(--key-green);grid-column:3/5;border:0}
.splash-name{position:absolute;top:62px;width:100%;text-align:center;font-weight:700;font-size:13px}
.splash-name small{font-size:9px}
.splash-brand{position:absolute;top:178px;width:100%;text-align:center}
.splash-brand .brand{justify-content:center;font-size:30px}
.splash-brand .brand b{width:24px;height:24px}
.tagline{font-size:9px;font-style:normal;font-weight:500;margin-top:4px}
.profile{height:126px;background:var(--navy);color:#fff;text-align:center;padding-top:19px}
.avatar{width:64px;height:64px;border-radius:50%;margin:0 auto;border:2px solid var(--blue);background:radial-gradient(circle at 50% 40%,#c99a78,#5a3d2b 70%)}
.profile p{font-size:7px;margin-top:6px}
.profile strong{display:block;font-size:11px;font-weight:600}
.tabs{display:flex;height:26px;font-size:7.5px;font-weight:500;box-shadow:0 1px 2px rgba(0,0,0,.06)}
.tabs span{flex:1;display:flex;align-items:center;justify-content:center;color:#999}
.tabs .on{color:var(--blue);border-bottom:2px solid var(--blue)}
.actions{display:grid;grid-template-columns:repeat(3,1fr);grid-auto-rows:60px}
.action{display:flex;flex-direction:column;align-items:center;justify-content:center;gap:4px;font-size:6.5px;font-weight:700;text-align:center;line-height:1.1;border-right:1px solid var(--line);border-bottom:1px solid var(--line)}
.action:nth-child(3n){border-right:0}
.action svg{width:24px;height:22px;fill:none;stroke:var(--navy);stroke-width:1.4;stroke-linecap:round;stroke-linejoin:round}
.dropdown{position:absolute;right:0;top:48px;width:96px;background:#fff;box-shadow:-2px 2px 6px rgba(0,0,0,.15);z-index:3}
.dropdown div{height:29px;display:flex;align-items:center;justify-content:space-between;padding:0 9px 0 16px;font-size:6px;color:#666;border-bottom:1px solid #f0f0f0}
.amount-line{margin:20px 19px 0;border-bottom:2px solid var(--blue);text-align:right;color:var(--blue);font-size:22px;font-weight:300;line-height:1.2}
.amount-line small{font-size:9px;color:#999;margin-left:4px}
.bars{display:flex;gap:5px;margin:18px 19px 0}
.bars span{flex:1;height:6px}
.bars.empty span{border:1px solid #aaa}
.sale-head{text-align:center;margin-top:28px;font-weight:700;font-size:13px}
.sale-amt{text-align:center;font-size:22px;font-weight:300;line-height:1.1}
.sale-amt small{font-size:13px}
.card-art{margin:30px auto 0;width:180px;height:72px;border-radius:6px;background:linear-gradient(90deg,#e7eef6,#d2deec)}
.prompt{text-align:center;color:var(--blue);font-weight:700;font-size:16.5px;line-height:1;margin-top:10px}
.card-bar{position:absolute;bottom:0;left:0;width:100%;height:28px;display:flex}
.schemes{flex:1;display:flex;align-items:center;gap:8px;padding-left:14px;font-size:8px;font-weight:700}
.manual{width:107px;background:var(--navy);color:#fff;display:flex;align-items:center;justify-content:center;gap:5px;font-size:8px;font-weight:500}
.manual i{width:9px;height:9px;background:
  radial-gradient(circle,#fff 1px,transparent 1.3px) 0 0/3px 3px}
.expiry{margin:12px 19px 0;border-bottom:2px solid var(--blue);text-align:center;color:var(--blue);font-size:16px;font-weight:300;line-height:1.4}
.expiry small{font-size:9px;color:#777}
.pin-title{padding:0 19px;font-weight:700;font-size:13px;margin-top:52px}
.pin-title big{font-size:18px}
.pin-title small{font-size:10px}
.result{position:absolute;top:48px;left:0;width:100%;height:332px;color:#fff;text-align:center}
.result.ok{background:var(--ok)}.result.busy{background:var(--busy)}.result.fail{background:var(--fail)}
.result p{font-size:8.5px;margin-top:24px}
.result h2{font-size:16px;font-weight:600;margin-top:78px}
.badge{width:70px;height:70px;border-radius:50%;background:#fff;margin:10px auto 0;display:flex;align-items:center;justify-content:center;border:3px solid rgba(255,255,255,.5);box-shadow:0 0 0 2px rgba(255,255,255,.4)}
.badge svg{width:38px;height:38px;fill:none;stroke-width:3.5;stroke-linecap:round;stroke-linejoin:round}
</style>
</head>
<body>

<!-- Row 1 -->
<section class="screen c1 r1">
  <div class="status"><i></i>50% 10:23</div>
  <div class="splash-name">PAYNOVA <small>(0.0.1)</small></div>
  <div class="splash-brand">
    <div class="brand"><b></b>NOVA</div>
    <p class="tagline">Your Payment Partner of Choice</p>
  </div>
</section>

<section class="screen c2 r1">
  <header class="header"><div class="status"><i></i>50% 10:23</div><div class="brand"><b></b>NOVA</div><div class="menu"><span></span><span></span><span></span></div></header>
  <div style="height:40px"></div>
  <div class="title">WELCOME</div>
  <div class="sub">Enter User Credentials:</div>
  <div class="field" style="margin-top:10px">USER ID</div>
  <div class="field" style="margin-top:14px">PASSWORD</div>
  <div class="keypad"><div>1</div><div>2</div><div>3</div><div class="zero">0</div><div>4</div><div>5</div><div>6</div><div>7</div><div>8</div><div>9</div><div class="k-x">✕</div><div class="k-back">⌫</div><div class="k-enter">⟵</div></div>
</section>

<section class="screen c3 r1">
  <header class="header"><div class="status"><i></i>50% 10:23</div><div class="battery"></div><div class="brand"><b></b>NOVA</div><div class="menu"><span></span><span></span><span></span></div></header>
  <div class="profile"><div class="avatar" role="img" aria-label="User profile photo"></div><p>Welcome,</p><strong>Username</strong></div>
  <div class="tabs"><span class="on">MAIN</span><span>ADMIN</span></div>
  <div class="actions">
    <div class="action"><svg viewBox="0 0 24 22"><rect x="2" y="3" width="20" height="15" rx="2"/><path d="M2 8h20M5 13h6"/></svg>SALE</div>
    <div class="action"><svg viewBox="0 0 24 22"><path d="M3 7h17l-4-4M21 15H4l4 4"/></svg>REVERSAL</div>
    <div class="action"><svg viewBox="0 0 24 22"><path d="M17 6a8 8 0 1 1-10 0M7 2v4H3"/></svg>REFUND</div>
    <div class="action"><svg viewBox="0 0 24 22"><path d="M12 1l9 4v6c0 5-4 9-9 10-5-1-9-5-9-10V5z"/><rect x="8" y="10" width="8" height="6"/><path d="M10 10V8a2 2 0 0 1 4 0v2"/></svg>PRE-AUTH</div>
    <div class="action"><svg viewBox="0 0 24 22"><rect x="3" y="2" width="18" height="18" rx="4"/><path d="M8 11l3 3 5-6"/></svg>COMPLETION</div>
    <div class="action"><svg viewBox="0 0 24 22"><path d="M1 7l5-3 6 3 6-3 5 3M4 6l6 8 2-1 2 2 2-1 4-8M9 11l3 3"/></svg>RECONCILIATION</div>
    <div class="action"><svg viewBox="0 0 24 22"><rect x="6" y="2" width="12" height="5"/><rect x="2" y="7" width="20" height="9" rx="1"/><rect x="6" y="13" width="12" height="7"/></svg>REPRINT<br>MANAGER</div>
  </div>
</section>

<section class="screen c4 r1">
  <header class="header"><div class="status"><i></i>50% 10:23</div><div class="battery"></div><div class="brand"><b></b>NOVA</div><div class="menu"><span></span><span></span><span></span></div></header>
  <nav class="dropdown">
    <div>LOGOUT <span>⇥</span></div><div>SETTINGS <span>›</span></div><div>WIFI SETTINGS <span>›</span></div><div>DATA SETTINGS <span>›</span></div><div>INPUT SETTINGS <span>›</span></div><div>APP SETTINGS <span>›</span></div>
  </nav>
  <div class="profile"><div class="avatar" role="img" aria-label="User profile photo"></div><p>Welcome,</p><strong>Username</strong></div>
  <div class="tabs"><span class="on">MAIN</span><span>ADMIN</span></div>
  <div class="actions">
    <div class="action"><svg viewBox="0 0 24 22"><rect x="2" y="3" width="20" height="15" rx="2"/><path d="M2 8h20M5 13h6"/></svg>SALE</div>
    <div class="action"><svg viewBox="0 0 24 22"><path d="M3 7h17l-4-4M21 15H4l4 4"/></svg>REVERSAL</div>
    <div class="action"><svg viewBox="0 0 24 22"><path d="M17 6a8 8 0 1 1-10 0M7 2v4H3"/></svg>REFUND</div>
    <div class="action"><svg viewBox="0 0 24 22"><path d="M12 1l9 4v6c0 5-4 9-9 10-5-1-9-5-9-10V5z"/><rect x="8" y="10" width="8" height="6"/><path d="M10 10V8a2 2 0 0 1 4 0v2"/></svg>PRE-AUTH</div>
    <div class="action"><svg viewBox="0 0 24 22"><rect x="3" y="2" width="18" height="18" rx="4"/><path d="M8 11l3 3 5-6"/></svg>COMPLETION</div>
    <div class="action"><svg viewBox="0 0 24 22"><path d="M1 7l5-3 6 3 6-3 5 3M4 6l6 8 2-1 2 2 2-1 4-8M9 11l3 3"/></svg>RECONCILIATION</div>
    <div class="action"><svg viewBox="0 0 24 22"><rect x="6" y="2" width="12" height="5"/><rect x="2" y="7" width="20" height="9" rx="1"/><rect x="6" y="13" width="12" height="7"/></svg>REPRINT<br>MANAGER</div>
  </div>
</section>

<!-- Row 2 -->
<section class="screen c1 r2">
  <header class="header"><div class="status"><i></i>50% 10:23</div><div class="brand"><b></b>NOVA</div></header>
  <div style="height:48px"></div>
  <div class="title">SALE</div>
  <div class="sub">Enter Amount:</div>
  <div class="amount-line">0.00<small>GBP</small></div>
  <div class="keypad"><div>1</div><div>2</div><div>3</div><div class="zero">0</div><div>4</div><div>5</div><div>6</div><div>7</div><div>8</div><div>9</div><div class="k-x">✕</div><div class="k-back">⌫</div><div class="k-enter">⟵</div></div>
</section>

<section class="screen c2 r2">
  <header class="header"><div class="status"><i></i>50% 10:23</div><div class="brand"><b></b>NOVA</div></header>
  <div class="bars"><span style="background:#5b9be8"></span><span style="background:#f5e21c"></span><span style="background:#2ecc8f"></span><span style="background:#e84a4f"></span></div>
  <div class="sale-head">SALE</div>
  <div class="sale-amt">0.01<small>GBP</small></div>
  <div class="card-art" role="img" aria-label="Illustration of tapping, swiping and inserting a card"></div>
  <div class="prompt">TAP, SWIPE or INSERT<br>your card</div>
  <div class="card-bar"><div class="schemes"><span>CARDA</span><span>ORBIS</span></div><div class="manual"><i></i>MANUAL ENTRY</div></div>
</section>

<section class="screen c3 r2">
  <header class="header"><div class="status"><i></i>50% 10:23</div><div class="brand"><b></b>NOVA</div></header>
  <div class="bars empty"><span></span><span></span><span></span><span></span></div>
  <div class="sale-head">SALE</div>
  <div class="sale-amt">0.01<small>GBP</small></div>
  <div class="card-art" role="img" aria-label="Illustration of tapping, swiping and inserting a card"></div>
  <div class="prompt">TAP, SWIPE or INSERT<br>your card</div>
  <div class="card-bar"><div class="schemes"><span>CARDA</span><span>ORBIS</span></div><div class="manual"><i></i>MANUAL ENTRY</div></div>
</section>

<section class="screen c4 r2">
  <header class="header"><div class="status"><i></i>50% 10:23</div><div class="brand"><b></b>NOVA</div></header>
  <div style="height:42px"></div>
  <div class="title">SALE</div>
  <div class="sub">Enter Card Information:</div>
  <div class="field" style="margin-top:10px">CARD #</div>
  <div class="expiry"><small>EXPIRY DATE</small> MM/YY</div>
  <div class="keypad"><div>1</div><div>2</div><div>3</div><div class="zero">0</div><div>4</div><div>5</div><div>6</div><div>7</div><div>8</div><div>9</div><div class="k-x">✕</div><div class="k-back">⌫</div><div class="k-enter">⟵</div></div>
</section>

<!-- Row 3 -->
<section class="screen c1 r3">
  <header class="header"><div class="status"><i></i>50% 10:23</div><div class="brand"><b></b>NOVA</div></header>
  <div class="pin-title">SALE: <big>1.00</big><small>GBP</small></div>
  <div class="sub">Enter Pin:</div>
  <div class="field" style="margin-top:20px;font-size:19px">PIN#</div>
  <div class="keypad"><div>1</div><div>2</div><div>3</div><div class="zero">0</div><div>4</div><div>5</div><div>6</div><div>7</div><div>8</div><div>9</div><div class="k-x">✕</div><div class="k-back">⌫</div><div class="k-enter">⟵</div></div>
</section>

<section class="screen c2 r3">
  <header class="header"><div class="status"><i></i>50% 10:23</div><div class="brand"><b></b>NOVA</div></header>
  <div class="result ok"><p>TEST CONNECTED</p><h2>AUTHORISED</h2>
    <div class="badge"><svg viewBox="0 0 40 40" style="stroke:var(--ok)"><path d="M8 21l8 8 16-17"/></svg></div></div>
</section>

<section class="screen c3 r3">
  <header class="header"><div class="status"><i></i>50% 10:23</div><div class="brand"><b></b>NOVA</div></header>
  <div class="result busy"><p>TEST CONNECTED</p><h2>PROCESSING</h2>
    <div class="badge"><svg viewBox="0 0 40 40" style="stroke:var(--busy)"><path d="M10 6h20M10 34h20M13 6c0 9 14 10 14 14s-14 5-14 14M27 6c0 9-14 10-14 14s14 5 14 14"/></svg></div></div>
</section>

<section class="screen c4 r3">
  <header class="header"><div class="status"><i></i>50% 10:23</div><div class="brand"><b></b>NOVA</div></header>
  <div class="result fail"><p>TEST CONNECTED</p><h2>ERROR</h2>
    <div class="badge"><svg viewBox="0 0 40 40" style="stroke:var(--fail)"><path d="M10 10l20 20M30 10L10 30"/></svg></div></div>
</section>

</body>
</html>
```